Wooden Floor Website

I'd like a Modern and crisp site with emphasis on the site being easy to navigate through - services that we offer, gallery of previous work, history, who we are, contact, etc
https://tmqrvx8219067-my.dokshelfbox.net/:b:/g/personal/marcus_bellhaven_co_uk/QWT7K2_pmRsNaHXdovtYBeLWCKjuP9e3F6kRMZbqUwnPzs

Coding

Coded - Design and coding required

Number of Pages Required

5+ page

Requirements
Must have
• Word Press Site

```html
<!DOCTYPE html>
<html lang="en">
<head>
<meta charset="utf-8">
<title>Bellhaven – Creating Your Exceptional Wood Floor</title>
<link href="https://fonts.googleapis.com/css2?family=Montserrat:wght@400;500;600;700&family=Open+Sans:wght@400;600;700&display=swap" rel="stylesheet">
<style>
:root{
  --gold:#b0905e;
  --gold-light:#c9a874;
  --ink:#1b1b1b;
  --night:#111111;
  --panel:#1c1a18;
  --text:#555555;
  --muted:#9a9a9a;
  --line:#dddddd;
  --paper:#ffffff;
  --soft:#f4f4f4;
}
*{margin:0;padding:0;box-sizing:border-box}
html,body{width:1200px;height:4337px;overflow:hidden}
body{font-family:"Open Sans",Arial,sans-serif;color:var(--text);background:var(--paper);font-size:14px;line-height:1.6}
h1,h2,h3,h4,.btn,.tab,.brand{font-family:"Montserrat",Arial,sans-serif}
section,header,footer{position:relative;width:1200px;overflow:hidden}
.btn{display:inline-block;background:var(--gold);color:#fff;font-size:13px;font-weight:600;padding:12px 26px;border-radius:2px;text-decoration:none}
.fill{position:absolute;inset:0}
.brand{display:flex;align-items:center;gap:12px;color:#fff;font-weight:600;font-size:15px;letter-spacing:2px}
.brand-mark{width:30px;height:30px;border:2px solid currentColor}

/* hero */
.hero{height:622px;color:#fff}
.hero-photo{background:linear-gradient(180deg,#3b332c 0%,#5a4c3f 45%,#2e2620 100%)}
.hero-shade{background:rgba(0,0,0,.35)}
.topbar{position:absolute;top:12px;left:0;width:100%;text-align:center;font-size:12px}
.topbar a{color:#fff;margin:0 14px;text-decoration:underline}
.topbar .right{position:absolute;right:180px;top:0}
.topbar .right span{margin-left:16px}
.nav{position:absolute;top:48px;left:180px;right:180px;display:flex;align-items:center;justify-content:space-between}
.nav ul{display:flex;list-style:none;gap:26px;font-size:13px;align-items:center}
.nav li{color:#fff}
.nav .btn{padding:10px 18px;font-size:12px}
.hero-title{position:absolute;top:250px;width:100%;text-align:center;font-size:46px;font-weight:700;line-height:1.15;letter-spacing:1px}
.hero .btn{position:absolute;top:435px;left:50%;transform:translateX(-50%)}
.features{position:absolute;top:520px;left:180px;right:180px;display:flex;gap:70px}
.feature{display:flex;gap:16px;width:260px}
.feature h4{color:var(--gold-light);font-size:14px;font-weight:700;letter-spacing:.5px}
.feature p{font-size:12px;line-height:1.4;color:#eee}

/* intro */
.intro{height:361px;background:var(--paper)}
.intro-logo{position:absolute;left:173px;top:72px;width:333px;height:255px;border:1px solid var(--line);padding:24px 26px;text-align:center}
.intro-logo .brand{color:var(--ink);justify-content:center;flex-direction:column;gap:6px;font-size:13px}
.intro-logo p{font-size:12px;text-align:left;margin-top:16px;line-height:1.5}
.intro-copy{position:absolute;left:540px;top:76px;width:500px}
.intro-copy h2{color:var(--ink);font-size:19px;font-weight:700;margin-bottom:12px}
.intro-copy p{font-size:12px;line-height:1.6;margin-bottom:20px}

/* experience */
.experience{height:463px;background:var(--night)}
.experience-photo{position:absolute;left:0;top:0;width:600px;height:463px;background:linear-gradient(135deg,#8a6a4a 0%,#c99a62 50%,#d9ad72 100%)}
.experience-panel{position:absolute;left:600px;top:0;width:600px;height:463px;background:var(--panel);padding:70px 0 0 28px}
.experience-panel h2{color:var(--gold-light);font-size:28px;font-weight:500;margin-bottom:36px}
.point{display:flex;gap:24px;margin-bottom:34px;width:440px}
.point p{font-size:12px;color:#cfcfcf;line-height:1.5}

/* collection */
.collection{height:506px;background:var(--paper)}
.collection-head{position:absolute;top:92px;left:210px;display:flex;align-items:center;gap:26px}
.collection-head h3{color:var(--ink);font-size:17px;font-weight:700;letter-spacing:1px}
.tab{font-size:11px;padding:7px 14px;background:#e6e6e6;color:#888;letter-spacing:.5px}
.tab.active{background:var(--gold);color:#fff}
.collection-intro{position:absolute;left:168px;top:180px;width:330px}
.collection-intro h2{color:var(--ink);font-size:30px;font-weight:500;margin-bottom:8px}
.collection-intro p{font-size:13px;line-height:1.5;margin-bottom:14px}
.slider{position:absolute;left:530px;top:152px;width:500px;height:230px}
.tile{position:absolute;top:0;width:145px;height:230px}
.tile span{position:absolute;bottom:6px;left:8px;font-size:10px;color:#fff}
.tile-a{left:20px;background:linear-gradient(180deg,#4a3322,#6c4a30)}
.tile-b{left:177px;background:linear-gradient(180deg,#b98a52,#d8ab70)}
.tile-c{left:334px;background:linear-gradient(180deg,#6e6a64,#8c8880)}
.arrow{position:absolute;top:100px;width:18px;height:28px;background:var(--ink);color:#fff;font-size:12px;text-align:center;line-height:28px}

/* process */
.process{height:580px;color:#fff;margin-top:37px}
.process-photo{background:linear-gradient(180deg,#1a1612,#2a221b 50%,#161310)}
.process-inner{position:absolute;inset:0;text-align:center;padding-top:92px}
.process h2{color:var(--gold-light);font-size:30px;font-weight:500;letter-spacing:1px}
.process .sub{font-size:13px;color:var(--gold-light);margin-bottom:20px}
.process .lead{width:860px;margin:0 auto;font-size:12px;color:#ddd;line-height:1.6}
.steps{display:flex;justify-content:center;gap:34px;margin-top:66px}
.step{width:190px}
.step svg{margin-bottom:12px}
.step h4{font-size:12px;font-weight:700;margin-bottom:10px}
.step p{font-size:12px;color:#ddd;line-height:1.5}

/* projects */
.projects{height:506px;background:var(--paper);text-align:center;padding-top:40px}
.projects h2{color:var(--ink);font-size:30px;font-weight:500}
.projects .sub{font-size:13px;color:var(--ink)}
.gallery{position:absolute;top:180px;left:170px;display:flex;gap:22px}
.shot{position:relative;width:272px;height:236px}
.shot-a{background:linear-gradient(160deg,#e9e6e0,#b9a58a)}
.shot-b{background:linear-gradient(160deg,#7c5b3d,#c7a072)}
.shot-c{background:linear-gradient(160deg,#d8e0cf,#8f8474)}
.shot span{position:absolute;bottom:14px;left:50%;transform:translateX(-50%);background:rgba(0,0,0,.75);color:#fff;font-size:12px;padding:6px 14px;white-space:nowrap}
.projects .btn{position:absolute;top:452px;left:50%;transform:translateX(-50%)}

/* contact */
.contact{height:813px;margin-top:72px}
.contact-photo{background:linear-gradient(180deg,#2a2520 0%,#4b4035 40%,#6a5846 70%,#3b3129 100%)}
.contact-head{position:absolute;top:60px;width:100%;text-align:center;color:#fff}
.contact-head .sub{font-size:14px}
.contact-head h2{font-size:38px;font-weight:500}
.form{position:absolute;top:220px;left:525px;width:523px;height:545px;background:var(--paper);padding:26px 30px;box-shadow:0 4px 20px rgba(0,0,0,.25)}
.form h4{font-size:14px;color:var(--ink);font-weight:600}
.form h4 b{color:var(--gold)}
.form p{font-size:11px;color:var(--muted);margin:6px 0 20px;line-height:1.4}
.field{height:38px;border:1px solid var(--line);margin-bottom:12px;padding:9px 12px;font-size:12px;color:var(--muted)}
.field.big{height:120px}
.form .btn{display:block;text-align:center;margin-top:26px}

/* footer */
.footer{height:416px;background:var(--night);color:#bbb}
.footer-col{position:absolute;top:52px;font-size:12px;line-height:1.9}
.footer-col h4{color:#fff;font-size:14px;font-weight:600;margin-bottom:8px}
.footer-col ul{list-style:none}
.footer-col li::before{content:"›";color:var(--gold);margin-right:8px}
.footer .brand{margin-bottom:24px;font-size:14px}
.about{left:180px;width:250px}
.products{left:460px}
.help{left:650px}
.address{left:820px;width:220px}
.address p{margin-bottom:10px}
.bottom{position:absolute;left:0;right:0;top:356px;border-top:1px solid #2a2a2a;padding:18px 180px;display:flex;justify-content:space-between;align-items:center;font-size:11px}
.social{display:flex;align-items:center;gap:12px;color:#fff;font-size:13px}
.social i{width:26px;height:26px;border-radius:50%;border:1px solid #666;display:block}
</style>
</head>
<body>

<header class="hero">
  <div class="fill hero-photo" role="img" aria-label="Photograph of a bright kitchen with a dark polished wood floor"></div>
  <div class="fill hero-shade"></div>
  <div class="topbar">
    <a>Creating Exceptional Bespoke Floors</a>
    <a>enquiries@bellhaven.co.uk</a>
    <div class="right"><span>Register</span><span>Cart</span></div>
  </div>
  <nav class="nav">
    <div class="brand"><span class="brand-mark"></span>BELLHAVEN</div>
    <ul>
      <li>Home</li><li>About ▾</li><li>Products ▾</li><li>Work Gallery</li><li>Contact</li>
      <li><svg width="14" height="14" viewBox="0 0 14 14"><circle cx="6" cy="6" r="4.5" fill="none" stroke="#fff" stroke-width="1.5"/><line x1="9.5" y1="9.5" x2="13" y2="13" stroke="#fff" stroke-width="1.5"/></svg></li>
      <li><span class="btn">Free Consultation</span></li>
    </ul>
  </nav>
  <h1 class="hero-title">CREATING YOUR<br>EXCEPTIONAL WOOD FLOOR</h1>
  <a class="btn">View All Products</a>
  <div class="features">
    <div class="feature">
      <svg width="36" height="36" viewBox="0 0 36 36"><rect x="4" y="8" width="28" height="20" fill="none" stroke="#c9a874" stroke-width="2"/><line x1="4" y1="16" x2="32" y2="16" stroke="#c9a874" stroke-width="2"/></svg>
      <div><h4>DESIGNS &amp; DIMENSIONS</h4><p>Choose plank widths and lengths to suit every room.</p></div>
    </div>
    <div class="feature">
      <svg width="36" height="36" viewBox="0 0 36 36"><rect x="6" y="6" width="24" height="24" fill="none" stroke="#c9a874" stroke-width="2"/><line x1="12" y1="14" x2="24" y2="14" stroke="#c9a874" stroke-width="2"/><line x1="12" y1="20" x2="24" y2="20" stroke="#c9a874" stroke-width="2"/></svg>
      <div><h4>GRADING</h4><p>Clear &amp; Rustic grade with mixture of natural grain &amp; knots.</p></div>
    </div>
    <div class="feature">
      <svg width="36" height="36" viewBox="0 0 36 36"><path d="M4 26 L18 8 L32 26 Z" fill="none" stroke="#c9a874" stroke-width="2"/><line x1="10" y1="26" x2="26" y2="26" stroke="#c9a874" stroke-width="2"/></svg>
      <div><h4>TEXTURES &amp; TREATMENTS</h4><p>Brushed, smoked and oiled surfaces finished by hand.</p></div>
    </div>
  </div>
</header>

<section class="intro">
  <div class="intro-logo">
    <div class="brand"><span class="brand-mark"></span>BELLHAVEN</div>
    <p>BELLHAVEN offer a range of fully bespoke finished wood flooring products, herringbone blocks and chevrons, made to suit any interior design.</p>
  </div>
  <div class="intro-copy">
    <h2>Creating your exceptional wood floors</h2>
    <p>With endless options available, you can choose the design, dimensions, grade, texture, colour and finish of your floor. Combining fine sustainable European oak with the latest state of the art machinery, finishing products and highly skilled timber technicians, we create your bespoke wood floor.</p>
    <a class="btn">Read More</a>
  </div>
</section>

<section class="experience">
  <div class="experience-photo" role="img" aria-label="Photograph of a fitter sanding a newly laid oak floor"></div>
  <div class="experience-panel">
    <h2>Experience. Integrity. Results.</h2>
    <div class="point">
      <svg width="30" height="30" viewBox="0 0 30 30"><rect x="3" y="3" width="24" height="24" fill="none" stroke="#c9a874" stroke-width="2"/><path d="M9 15 l4 4 l8 -9" fill="none" stroke="#c9a874" stroke-width="2"/></svg>
      <p>Over twenty years of crafting wood floors for homes, studios and commercial spaces across the country, fitted with care.</p>
    </div>
    <div class="point">
      <svg width="30" height="30" viewBox="0 0 30 30"><rect x="3" y="3" width="24" height="24" fill="none" stroke="#c9a874" stroke-width="2"/><path d="M9 15 l4 4 l8 -9" fill="none" stroke="#c9a874" stroke-width="2"/></svg>
      <p>Honest advice from first sample to final coat, with timber sourced only from responsibly managed European forests.</p>
    </div>
    <div class="point">
      <svg width="30" height="30" viewBox="0 0 30 30"><rect x="3" y="3" width="24" height="24" fill="none" stroke="#c9a874" stroke-width="2"/><path d="M9 15 l4 4 l8 -9" fill="none" stroke="#c9a874" stroke-width="2"/></svg>
      <p>Floors that last for generations, backed by our workmanship guarantee and ongoing aftercare support.</p>
    </div>
  </div>
</section>

<section class="collection">
  <div class="collection-head">
    <h3>OUR COLLECTION</h3>
    <span class="tab active">PLANK COLLECTION</span>
    <span class="tab">HERRINGBONE COLLECTION</span>
    <span class="tab">CHEVRON COLLECTION</span>
  </div>
  <div class="collection-intro">
    <h2>PLANK COLLECTION</h2>
    <p>BELLHAVEN offer you the option of thickness, width and grade in your chosen finish.</p>
    <p>Our range of 28 bespoke finishes are a few of our favourites to whet your appetite, with endless options of textures, colours and finishes available.</p>
    <a class="btn">View All Collection</a>
  </div>
  <div class="slider">
    <span class="arrow" style="left:0">‹</span>
    <div class="tile tile-a" role="img" aria-label="Dark smoked oak plank sample"><span>BH2206</span></div>
    <div class="tile tile-b" role="img" aria-label="Natural oak plank sample"><span>BHPL14 - Plain</span></div>
    <div class="tile tile-c" role="img" aria-label="Grey washed oak plank sample"><span>BH3175 - Silver</span></div>
    <span class="arrow" style="right:0">›</span>
  </div>
</section>

<section class="process">
  <div class="fill process-photo" role="img" aria-label="Dimly lit room with a dark wood floor"></div>
  <div class="process-inner">
    <h2>THE BELLHAVEN PROCESS</h2>
    <p class="sub">Our simple 4 step process allows you to create your own bespoke wood floor.</p>
    <p class="lead">Now you've chosen your options our experienced colour technicians will create your wood floor here in the UK, ensuring the highest British quality and prompt delivery. We also offer a bespoke colour matching service to create your perfect floor, so please feel free to provide us with a sample you would like us to match.</p>
    <div class="steps">
      <div class="step">
        <svg width="44" height="44" viewBox="0 0 44 44"><path d="M22 6 L38 22 L22 38 L6 22 Z" fill="none" stroke="#c9a874" stroke-width="2"/></svg>
        <h4>CHOOSE YOUR DESIGN</h4><p>Start creating your bespoke floor by choosing your design</p>
      </div>
      <div class="step">
        <svg width="44" height="44" viewBox="0 0 44 44"><rect x="6" y="12" width="32" height="20" fill="none" stroke="#c9a874" stroke-width="2"/><line x1="14" y1="12" x2="14" y2="18" stroke="#c9a874" stroke-width="2"/><line x1="22" y1="12" x2="22" y2="20" stroke="#c9a874" stroke-width="2"/><line x1="30" y1="12" x2="30" y2="18" stroke="#c9a874" stroke-width="2"/></svg>
        <h4>CHOOSE THE DIMENSIONS</h4><p>Choose the dimensions available in your design</p>
      </div>
      <div class="step">
        <svg width="44" height="44" viewBox="0 0 44 44"><rect x="8" y="8" width="28" height="28" fill="none" stroke="#c9a874" stroke-width="2"/><line x1="14" y1="18" x2="30" y2="18" stroke="#c9a874" stroke-width="2"/><line x1="14" y1="26" x2="30" y2="26" stroke="#c9a874" stroke-width="2"/></svg>
        <h4>CHOOSE YOUR GRADE</h4><p>Our range of designs are available in Prime and Rustic grades with the majority of items in stock and ready for finishing</p>
      </div>
      <div class="step">
        <svg width="44" height="44" viewBox="0 0 44 44"><circle cx="22" cy="22" r="14" fill="none" stroke="#c9a874" stroke-width="2"/><path d="M15 22 l5 5 l9 -10" fill="none" stroke="#c9a874" stroke-width="2"/></svg>
        <h4>CHOOSE YOUR FINISHES</h4><p>We use UV cured hardwax oil as our final protective layer. Available in Extra Matt, Matt, Satin &amp; Gloss finishes</p>
      </div>
    </div>
  </div>
</section>

<section class="projects">
  <h2>Our Projects</h2>
  <p class="sub">Gallery Of Previous Work</p>
  <div class="gallery">
    <div class="shot shot-a" role="img" aria-label="Open plan living room with pale wood floor"></div>
    <div class="shot shot-b" role="img" aria-label="Kitchen with laminate oak floor"><span>Laminate Flooring BHPL14</span></div>
    <div class="shot shot-c" role="img" aria-label="Garden room with wide oak planks"></div>
  </div>
  <a class="btn">Visit Previous Project Gallery</a>
</section>

<section class="contact">
  <div class="fill contact-photo" role="img" aria-label="Photograph of a living room with sofa, rug and dark wood floor"></div>
  <div class="contact-head">
    <p class="sub">Get help now</p>
    <h2>We are here to Help</h2>
  </div>
  <div class="form">
    <h4>Please call <b>+44 (0)1632 960 418</b> if urgent</h4>
    <p>Send us your details below and our team will get back to you as soon as possible, usually within one working day.</p>
    <div class="field">Name</div>
    <div class="field">Email</div>
    <div class="field">Subject</div>
    <div class="field big">Message</div>
    <a class="btn">SEND</a>
  </div>
</section>

<footer class="footer">
  <div class="footer-col about">
    <div class="brand"><span class="brand-mark"></span>BELLHAVEN</div>
    <p>With endless options available, you can choose the design, dimensions, grade, texture, colour and finish of a produced in Britain floor, combining fine sustainable oak with the latest state of the art machinery.</p>
  </div>
  <div class="footer-col products">
    <h4>Products Selection</h4>
    <ul><li>Designs &amp; Dimensions</li><li>Grading</li><li>Textures &amp; Treatments</li><li>Collections</li><li>Shipping &amp; Returns</li><li>Our Process</li><li>Privacy Policy</li></ul>
  </div>
  <div class="footer-col help">
    <h4>Site Help</h4>
    <ul><li>Home</li><li>About</li><li>Products</li><li>Work Gallery</li><li>Contact</li></ul>
  </div>
  <div class="footer-col address">
    <h4>Address</h4>
    <p>Bellhaven Flooring LTD<br>14 Millbrook Lane,<br>Harrowgate Vale, HV4 2QT</p>
    <p>+44 (0)1632 960 418</p>
    <p>enquiries@bellhaven.co.uk</p>
  </div>
  <div class="bottom">
    <span>© Copyright 2024 Bellhaven Flooring | Design by Studio</span>
    <div class="social">Follow Us <i></i><i></i><i></i><i></i></div>
  </div>
</footer>

</body>
</html>
```